engaging mobile application to encourage lifestyle change

We need an App that will help people get from Bloom 4 Joy. A weight loss program based on realistic and healthy lifestyle modifications. By learning portion control, healthy food choices, and with the encouragement to get moving.
We would like the design to be gender neutral but must be fun.
The final design must be easy to use and useful to our clients.

Target Market(s)

Health, Wellbeing, Weightloss

Industry/Entity Type

Weight

Font styles to use
Sans Serif

Requirements
Must have
• Hydration log, Weigh-ins with fat %, Food log, Location of meetings,lectures and weigh-ins, list of restaurants that comply with B4J, Fitness plan, Mall walk maps, daily motivational message.

```html
<!DOCTYPE html>
<html lang="en">
<head>
<meta charset="utf-8">
<title>Bloom 4 Joy – Welcome</title>
<link rel="stylesheet" href="https://fonts.googleapis.com/css2?family=Montserrat:wght@500;600;700&display=swap">
<style>
  :root {
    --screen-w: 719px;
    --screen-h: 1200px;
    --white: #ffffff;
    --veg-dark: #2b2a24;
    --veg-green: #4d6a3c;
    --veg-carrot: #a8643a;
    --veg-radish: #8e2a33;
    --plate-grey: #4a4e4f;
    --shade: rgba(20, 20, 18, 0.38);
    --orbit-red: #c85a58;
    --circle-blue: #2f4868;
  }
  * { box-sizing: border-box; margin: 0; padding: 0; }
  html, body {
    width: var(--screen-w);
    height: var(--screen-h);
    overflow: hidden;
    background: #ffffff;
  }
  body { font-family: "Montserrat", "Helvetica Neue", Arial, sans-serif; }

  .welcome-screen {
    position: relative;
    width: var(--screen-w);
    height: var(--screen-h);
    overflow: hidden;
    color: var(--white);
  }

  .produce-backdrop {
    position: absolute;
    inset: 0;
    background:
      radial-gradient(ellipse 45% 30% at 62% 76%, rgba(142, 42, 51, 0.85), transparent 70%),
      radial-gradient(ellipse 40% 35% at 28% 40%, rgba(168, 100, 58, 0.8), transparent 70%),
      radial-gradient(ellipse 50% 40% at 78% 30%, rgba(77, 106, 60, 0.85), transparent 70%),
      radial-gradient(ellipse 60% 30% at 40% 64%, rgba(77, 106, 60, 0.7), transparent 70%),
      linear-gradient(180deg, var(--veg-dark) 0%, var(--plate-grey) 70%, var(--veg-dark) 100%);
  }
  .produce-backdrop::after {
    content: "";
    position: absolute;
    inset: 0;
    background: var(--shade);
  }

  .brand {
    position: absolute;
    top: 300px;
    left: 0;
    width: 100%;
    text-align: center;
  }
  .brand-name {
    font-weight: 700;
    font-size: 52px;
    letter-spacing: -0.5px;
    line-height: 1;
  }
  .brand-tagline {
    margin-top: 16px;
    font-weight: 600;
    font-size: 11px;
    letter-spacing: 4px;
  }

  .auth-actions {
    position: absolute;
    left: 152px;
    width: 424px;
  }
  .outline-button {
    display: flex;
    align-items: center;
    justify-content: center;
    width: 100%;
    height: 68px;
    border: 3px solid var(--white);
    border-radius: 34px;
    background: transparent;
    color: var(--white);
    font-family: inherit;
    font-weight: 700;
    font-size: 22px;
  }
  .login-button { position: absolute; top: 490px; }
  .signup-button { position: absolute; top: 599px; }

  .social-button {
    position: absolute;
    top: 742px;
    height: 40px;
    width: 244px;
    border: none;
    border-radius: 4px;
    display: flex;
    align-items: center;
    justify-content: center;
    color: var(--white);
    font-family: inherit;
    font-weight: 600;
    font-size: 15px;
  }
  .orbit-button { left: 97px; background: var(--orbit-red); }
  .circle-button { left: 375px; background: var(--circle-blue); }
</style>
</head>
<body>
  <main class="welcome-screen">
    <div class="produce-backdrop" role="img" aria-label="Photo of fresh carrots, radishes and a small bowl of salt on a dark plate"></div>

    <header class="brand">
      <h1 class="brand-name">Bloom 4 Joy</h1>
      <p class="brand-tagline">GROW A LITTLE EVERY DAY</p>
    </header>

    <div class="auth-actions">
      <button class="outline-button login-button" type="button">LOG IN</button>
      <button class="outline-button signup-button" type="button">SIGN UP</button>
    </div>

    <button class="social-button orbit-button" type="button">ORBIT SIGN IN</button>
    <button class="social-button circle-button" type="button">CIRCLEBOOK SIGN IN</button>
  </main>
</body>
</html>
```